BrindleStaffing Business Card Design

We are a staffing company finding positions for dedicated nurses and physicians.

Target Market(s)

Business Professionals

Industry/Entity Type

Staffing

Contact Information for Business Card

Gregory Malden
Chairman
417 39th Crescent South
SAINT PETERSBURG FL 33719
813-555-0147 Mobile
813-555-0183 Fax
gmalden@brindlestaffing.example
www.brindlestaffing.example

Font styles to use
Sans Serif

Colors
fbee3e
f04a50
f37122

Requirements
Must have
• Logo Attached, see colors below. We'd like to see Yellow, Orange and Red.

```html
<!DOCTYPE html>
<html lang="en">
<head>
<meta charset="utf-8">
<title>BrindleStaffing Business Card</title>
<link rel="stylesheet" href="https://fonts.googleapis.com/css2?family=Poppins:wght@600&family=Lato:wght@400&display=swap">
<style>
  :root {
    --backdrop: #2b2b2c;
    --card: #0e0e0f;
    --yellow: #fbee3e;
    --orange: #f37122;
    --red: #f04a50;
    --white: #f2f2f2;
    --muted: #bdbdbd;
    --rule: #555;
  }
  * { margin: 0; padding: 0; box-sizing: border-box; }
  html, body { width: 1200px; height: 900px; overflow: hidden; }
  body {
    background: var(--backdrop);
    position: relative;
    font-family: "Lato", Arial, sans-serif;
  }
  .card {
    position: absolute;
    left: 290px;
    width: 620px;
    height: 350px;
    background: var(--card);
    overflow: hidden;
    box-shadow: 0 10px 30px rgba(0,0,0,0.45);
  }
  .card-front { top: 80px; }
  .card-back { top: 470px; }
  .edge-band {
    position: absolute;
    left: 0; right: 0; bottom: 0;
    height: 9px;
    background: linear-gradient(90deg, var(--yellow) 0 30%, var(--orange) 38% 60%, var(--red) 68% 100%);
  }
  .brand {
    position: absolute;
    left: 0; right: 0; top: 138px;
    display: flex;
    justify-content: center;
    align-items: center;
    gap: 12px;
  }
  .brand-dot {
    width: 16px; height: 16px;
    border-radius: 50%;
    background: var(--yellow);
  }
  .brand-name {
    font-family: "Poppins", Arial, sans-serif;
    font-weight: 600;
    font-size: 46px;
    letter-spacing: -1px;
    color: var(--orange);
  }
  .holder {
    position: absolute;
    left: 100px; top: 120px;
    width: 215px;
    text-align: right;
  }
  .holder-name {
    font-family: "Poppins", Arial, sans-serif;
    font-weight: 600;
    font-size: 25px;
    line-height: 32px;
    white-space: nowrap;
  }
  .holder-first { color: var(--yellow); }
  .holder-last { color: var(--orange); }
  .holder-title {
    margin-top: 2px;
    color: var(--muted);
    font-size: 14px;
    letter-spacing: 1px;
  }
  .divider {
    position: absolute;
    left: 330px; top: 112px;
    width: 1px; height: 80px;
    background: var(--rule);
  }
  .contact-list {
    position: absolute;
    left: 348px; top: 112px;
    list-style: none;
    color: var(--white);
    font-size: 15px;
    line-height: 20px;
  }
  .contact-list li { display: flex; align-items: center; gap: 7px; white-space: nowrap; }
  .contact-list svg { width: 12px; height: 12px; fill: var(--red); flex: none; }
  .address {
    position: absolute;
    left: 80px; top: 262px;
    color: var(--white);
    font-size: 15.5px;
  }
</style>
</head>
<body>
  <section class="card card-front">
    <div class="brand">
      <span class="brand-dot"></span>
      <span class="brand-name">BrindleStaffing</span>
    </div>
    <div class="edge-band"></div>
  </section>

  <section class="card card-back">
    <div class="holder">
      <h1 class="holder-name"><span class="holder-first">Gregory</span> <span class="holder-last">Malden</span></h1>
      <p class="holder-title">Chairman</p>
    </div>
    <div class="divider"></div>
    <ul class="contact-list">
      <li>
        <svg viewBox="0 0 12 12" aria-hidden="true"><path d="M1 3c0-1 1-2 5-2s5 1 5 2v1H8V3H4v1H1zM3 5h6l2 5H1z"/></svg>
        813-555-0147 Mobile
      </li>
      <li>
        <svg viewBox="0 0 12 12" aria-hidden="true"><path d="M3 0h6v3H3zM0 4h12v6h-2V8H2v2H0zM3 9h6v3H3z"/></svg>
        813-555-0183 Fax
      </li>
      <li>
        <svg viewBox="0 0 12 12" aria-hidden="true"><path d="M0 2h12v8H0zM1 3v.5l5 3 5-3V3z" fill-rule="evenodd"/></svg>
        gmalden@brindlestaffing.example
      </li>
      <li>
        <svg viewBox="0 0 12 12" aria-hidden="true"><circle cx="6" cy="6" r="6"/></svg>
        www.brindlestaffing.example
      </li>
    </ul>
    <p class="address">417 39th Crescent South SAINT PETERSBURG FL 33719</p>
    <div class="edge-band"></div>
  </section>
</body>
</html>
```